FItness Bootcamp Flyer

We need an A4 flyer to distribute on an advertising board, and also distribute in the mail.

It should contain a photo(s) of females exercising and having fun outdoors.

It should contain the following text and if you think it could be worded better please change as I'm just looking at getting people to come along:

- KestrelMove Studio Outdoor Bootcamp
Get moving, get fit and feel great

Commencing 19th May

Get results before the winter season
6 Week Bootcamp for $49. Limited numbers!
Or casual visit $10 per session

Now is the time to:
- Lose Weight and Tone-up
- Build Strength and Endurance
- Increase Cardio Fitness
- Improve Your Energy and Vitality
- Fun Varied and Exciting Training Programs
- ALL Fitness Levels

LADIES ONLY BOOTCAMP SUBIACO
Monday 6:30-7:15am, 8:30-9:15am
Wednesday 6:30-7:!5am, 8:30-9:15am
Friday 8:30-9:15am,

Register you place now on 0428 574 812 or email: kestrelmovestudio@fernmail.net

facebook.com/KestrelMove Studio

Target Market(s)

Females 20-60yrs

Industry/Entity Type

Advertising

Requirements
Nice to have
• - We like the words and style of the Harbourline Open Air Training flyer attached
- Also the Vanta Group brochure
- I like the colour Blue, Green, Pink. They don't all have to be used but at least one would be nice thank you

```html
<!DOCTYPE html>
<html lang="en">
<head>
<meta charset="utf-8">
<title>KestrelMove Studio – Ladies Only Bootcamp Flyer</title>
<link rel="stylesheet" href="https://fonts.googleapis.com/css2?family=Ubuntu:wght@300;400;500;700&display=swap">
<style>
  :root {
    --stage: #4b4b4b;
    --brand-blue: #0b4da0;
    --sun-yellow: #ffc700;
    --lime: #9cf200;
    --lime-text: #a4f21c;
    --white: #ffffff;
    --photo-light: #b9d98a;
    --photo-mid: #7fb04a;
    --photo-deep: #4f7f2c;
  }
  * { box-sizing: border-box; margin: 0; padding: 0; }
  html, body {
    width: 973px; height: 1200px; overflow: hidden;
    background: var(--stage);
    font-family: "Ubuntu", "Trebuchet MS", sans-serif;
  }
  .flyer {
    position: absolute; left: 175px; top: 159px;
    width: 623px; height: 881px;
    background: var(--brand-blue);
    overflow: hidden;
  }
  .photo {
    position: absolute; left: 0; top: 110px; width: 623px; height: 370px;
    background:
      radial-gradient(ellipse at 75% 45%, #e8d3bf 0 8%, transparent 22%),
      linear-gradient(115deg, var(--photo-deep) 0%, var(--photo-mid) 35%, var(--photo-light) 60%, var(--photo-mid) 100%);
  }
  .waves { position: absolute; left: 0; top: 0; width: 623px; height: 881px; }
  .brand {
    position: absolute; left: 65px; top: 42px;
    font-weight: 300; font-size: 36px; letter-spacing: 0.5px;
    color: var(--white);
  }
  .headline {
    position: absolute; left: 62px; top: 192px;
    font-weight: 500; font-size: 44px; line-height: 41px;
    color: var(--brand-blue);
    letter-spacing: -0.5px;
  }
  .start-date {
    position: absolute; left: 68px; top: 327px;
    background: var(--brand-blue); color: var(--sun-yellow);
    font-size: 15px; line-height: 17px; padding: 0 3px;
  }
  .start-date b { font-weight: 700; }
  .details {
    position: absolute; left: 71px; top: 513px; width: 520px;
    color: var(--white);
  }
  .offer { color: var(--lime-text); font-size: 15px; line-height: 20px; }
  .offer-limited { color: var(--lime-text); font-size: 15px; line-height: 26px; }
  .offer-limited strong { font-size: 19px; font-weight: 700; }
  .benefits-title { color: var(--lime-text); font-weight: 700; font-size: 15px; line-height: 20px; }
  .benefits { list-style: none; font-size: 15px; line-height: 19.4px; }
  .benefits li::before { content: "- "; }
  .session-title {
    margin-top: 10px;
    color: var(--sun-yellow); font-weight: 500; font-size: 24px; line-height: 30px;
    letter-spacing: 0.3px;
  }
  .timetable { margin-left: 10px; border-collapse: collapse; font-size: 15px; line-height: 19px; }
  .timetable th { color: var(--lime-text); font-weight: 400; text-align: left; padding-right: 4px; }
  .timetable td { color: var(--white); }
  .register {
    margin-top: 20px; margin-left: 9px;
    font-size: 21px; line-height: 28px; color: var(--white);
  }
  .register strong { color: var(--lime-text); font-weight: 700; }
  .contact {
    margin-left: 9px; display: flex; align-items: center;
    font-size: 18px; line-height: 28px; color: var(--white);
  }
  .contact .marker {
    display: inline-block; width: 15px; height: 15px;
    background: var(--white); border-radius: 2px; margin-right: 3px;
  }
  .contact .marker + span + .marker { margin-left: 6px; }
</style>
</head>
<body>
  <main class="flyer">
    <div class="photo" role="img" aria-label="Photo of smiling women stretching arms overhead during an outdoor fitness class in a green park"></div>

    <svg class="waves" viewBox="0 0 623 881" aria-hidden="true">
      <path d="M0,0 H623 V132 C450,112 220,150 0,178 Z" fill="var(--lime)"/>
      <path d="M0,0 H623 V98 C450,118 220,140 0,137 Z" fill="var(--sun-yellow)"/>
      <path d="M0,0 H623 V60 C450,108 200,122 0,96 Z" fill="var(--brand-blue)"/>
      <path d="M0,455 C200,420 450,395 623,402 V881 H0 Z" fill="var(--lime)"/>
      <path d="M0,472 C200,440 450,428 623,440 V881 H0 Z" fill="var(--sun-yellow)"/>
      <path d="M0,516 C150,472 400,448 623,482 V881 H0 Z" fill="var(--brand-blue)"/>
    </svg>

    <div class="brand">KESTRELMOVE STUDIO</div>

    <h1 class="headline">get moving,<br>get fit and<br>feel great</h1>
    <div class="start-date">COMMENCING <b>19TH</b> MAY</div>

    <section class="details">
      <p class="offer">Get results before the winter season 6 Week Bootcamp for $49.</p>
      <p class="offer-limited"><strong>Limited numbers!</strong> Or casual visit $10 per session</p>
      <p class="benefits-title">Now is the time to:</p>
      <ul class="benefits">
        <li>Lose Weight and Tone-up</li>
        <li>Build Strength and Endurance</li>
        <li>Increase Cardio Fitness</li>
        <li>Improve Your Energy and Vitality</li>
        <li>Fun Varied and Exciting Training Programs</li>
        <li>ALL Fitness Levels</li>
      </ul>

      <h2 class="session-title">LADIES ONLY BOOTCAMP SUBIACO</h2>
      <table class="timetable">
        <tr><th>Monday</th><td>6:30-7:15am, 8:30-9:15am</td></tr>
        <tr><th>Wednesday</th><td>6:30-7:!5am, 8:30-9:15am</td></tr>
        <tr><th>Friday</th><td>8:30-9:15am,</td></tr>
      </table>

      <p class="register">REGISTER YOU PLACE NOW ON <strong>0428 574 812</strong></p>
      <p class="contact">
        <span class="marker"></span><span>kestrelmovestudio@fernmail.net</span>
        <span class="marker"></span><span>/KestrelMove Studio</span>
      </p>
    </section>
  </main>
</body>
</html>
```